Photography and Political Commentary Blog

Hi there!
I'd like to build a clean, simple, yet visually appealing blog using a theme similar to this: http://www.brightlayouts.net/demo/?theme=TheFrame. I’m looking to work with a designer who has a modern aesthetic who can work with me to create a great blog. Hopefully that’s you!
Details:
The aim would be for the blog to be simple and clean, with each post represented by a picture, title and short summary as with ‘The Frame’ theme. These post summaries would be displayed in a single area without sidebars or columns.
There would be a home page in addition to four pages that you can access from a menu panel. These subordinate pages would be very similar if not the same in style to the main page. The subordinate pages would be:
- Politics
- Security
- Photography
- Music
For each page:
Politics and Security. These pages would be in a traditional blog format with the ability to post, hyperlink, comment etc. Posts would typically be 200-400 words. I am in the military and actively involved in politics and would like to be able to post my thoughts on issues ‘Quick Thoughts on Big Ideas’, and hyperlink to articles with short personal comments.
Photography. The photography main page would be like the homepage with each post represented by a single photo, title and summary (as per ‘The Frame’ theme). The individual posts would need to be able to display photo galleries in a grid, with the ability to click on individual photos to view them in high definition. I am open to the use of different widgets to best display the photos. Typically, each gallery would have 6-10 photos. I am a keen amateur (semi-professional?) photographer. This page would showcase small galleries of my artistic work as opposed to large journal/travel style galleries.
Music. This page is a simply way for me to post links to songs I like from ClipNest, Reelo, Tunebarn etc.
I like the clean style and typeface of the following blogs:
http://www.gallowmark.com/
http://www.thecusp.com/
http://quenlatori.com/
http://hollyonstuffs.com/
http://whatmysisterpicked.jotpage.com/
I like color palates similar to these –
http://www.huevault.com/palette/482137/Moss_Heron
http://www.huevault.com/palette/2958/Cedar_Nine
The first file I have attached is a logo that uses the types of colors and look I'd like to achieve. The second file I have attached has the type of font I'd like to use (something in the 'Sans' family: http://www.typecrate.com/fonts/category/sans/
In general, I like the use of red highlights with other neutral tones (greys, blues etc) but I’m open to your ideas!
For the function of the blog, the homepage would be a sequential summary of the posts from each of the subsections (politics, security, photography and music). I'd like this to be grouped so you can see 3 or 4 of the most recent posts from each section - but I'm open to ideas. The main pages for each subsection would be the same: a sequential summary of the posts for that area. If using Wordpress, I would like to be able to do this automatically, for instance by allocating ‘categories’ to each post that sort the posts into their respective sections.
The site name will be gavinmarsh.com.au. Any logos or headings would be my name ‘Gavin Marsh’. I already own the domain name.
The main aim for this project is for it to be clean, simple and elegant (in a modern way). Something that people can open and easily navigate without clutter, yet is visually appealing.
Thanks for taking the time to read this brief and really looking forward to working with you!
Cheers!
Gav

```html
<!DOCTYPE html>
<html lang="en">
<head>
<meta charset="utf-8">
<title>Gavin Marsh</title>
<link href="https://fonts.googleapis.com/css2?family=Oswald:wght@300;400&family=Fjalla+One&family=Arimo:wght@400;700&display=swap" rel="stylesheet">
<style>
:root{
  --sand:#f0d9ab;
  --paper:#f6efe6;
  --red:#ff2a00;
  --title-red:#ef3a12;
  --brown:#3d1a00;
  --grey:#7a7572;
  --white:#ffffff;
}
*{margin:0;padding:0;box-sizing:border-box}
html,body{width:1200px;height:2466px;overflow:hidden}
body{position:relative;background:var(--sand);font-family:"Arimo",Arial,sans-serif;color:var(--brown)}

.site-header{position:absolute;left:0;top:0;width:1200px;height:151px}
.brand{position:absolute;left:18px;top:20px;font-family:"Oswald",sans-serif;font-weight:400;font-size:94px;line-height:1;color:var(--brown);letter-spacing:1px}
.social{position:absolute;display:flex;gap:17px}
.social-header{left:840px;top:56px}
.social-item{width:52px;height:52px;border-radius:50%;display:flex;align-items:center;justify-content:center;font-family:"Arimo",sans-serif;font-weight:700;font-size:10px;color:var(--sand)}
.social-header .social-item{background:var(--brown)}
.social-footer .social-item{background:var(--red);color:var(--white)}

.main-nav{position:absolute;left:14px;top:151px;width:1186px;height:54px;background:var(--red);border-bottom:3px solid var(--brown)}
.nav-item{position:absolute;top:0;height:51px;line-height:51px;font-family:"Oswald",sans-serif;font-weight:300;font-size:30px;color:var(--white);text-transform:uppercase}
.nav-item.is-active{left:1px;width:136px;background:var(--brown);text-align:center}
.search{position:absolute;left:819px;top:7px;width:346px;height:40px;display:flex}
.search-field{flex:1;background:var(--sand);font-family:"Fjalla One",sans-serif;font-size:22px;line-height:40px;padding-left:12px;color:var(--brown)}
.search-button{width:55px;background:var(--brown);display:flex;align-items:center;justify-content:center}

.category{position:absolute;left:15px;width:1165px;height:474px;background:var(--paper)}
.category-label{position:absolute;left:0;top:26px;width:261px;height:46px;background:var(--red);color:var(--white);font-family:"Fjalla One",sans-serif;font-size:31px;line-height:46px;padding-left:31px;text-transform:uppercase}
.posts{position:absolute;left:38px;top:102px;display:flex;gap:58px}
.post{width:322px}
.post-image{width:322px;height:215px;border:3px solid var(--brown)}
.post-title{margin-top:9px;font-family:"Fjalla One",sans-serif;font-size:23px;line-height:30px;color:var(--title-red);white-space:nowrap;overflow:hidden}
.post-summary{margin-top:4px;font-size:14.5px;line-height:17.6px;color:var(--grey);height:71px;overflow:hidden}

.site-footer{position:absolute;left:0;top:2185px;width:1200px;height:281px;background:var(--brown);color:var(--white)}
.newsletter{position:absolute;left:21px;top:36px;width:580px}
.footer-heading{font-size:20px;line-height:26px;font-weight:400}
.footer-heading strong{font-weight:700}
.newsletter p{margin-top:6px;font-size:14px;line-height:18px}
.newsletter-form{position:absolute;left:18px;top:116px;display:flex;gap:16px}
.newsletter-input{width:459px;height:38px;background:var(--sand)}
.newsletter-button{width:137px;height:38px;background:var(--red);color:var(--white);font-size:20px;line-height:38px;text-align:center}
.location{position:absolute;left:838px;top:36px}
.location address{margin-top:6px;font-style:normal;font-size:14px;line-height:18px}
.social-footer{left:834px;top:153px}
.footer-rule{position:absolute;left:0;top:213px;width:1200px;height:1px;background:#8c6f58}
.footer-nav{position:absolute;left:21px;top:236px;display:flex;gap:22px;font-size:14px}
.copyright{position:absolute;left:840px;top:236px;font-size:13px}
.copyright strong{font-weight:700}
</style>
</head>
<body>

<header class="site-header">
  <div class="brand">GAVIN MARSH</div>
  <div class="social social-header">
    <span class="social-item">Chirp</span>
    <span class="social-item">Facet</span>
    <span class="social-item">Plusly</span>
    <span class="social-item">Pinora</span>
    <span class="social-item">Linkro</span>
  </div>
</header>

<nav class="main-nav">
  <span class="nav-item is-active">Home</span>
  <span class="nav-item" style="left:150px">Photography</span>
  <span class="nav-item" style="left:372px">Politics</span>
  <span class="nav-item" style="left:523px">Security</span>
  <span class="nav-item" style="left:683px">Music</span>
  <div class="search">
    <div class="search-field">search</div>
    <div class="search-button">
      <svg width="26" height="26" viewBox="0 0 26 26"><circle cx="10" cy="10" r="6.5" fill="none" stroke="#fff" stroke-width="3"/><line x1="15" y1="15" x2="23" y2="23" stroke="#fff" stroke-width="4" stroke-linecap="round"/></svg>
    </div>
  </div>
</nav>

<section class="category" style="top:225px">
  <h2 class="category-label">Politics</h2>
  <div class="posts">
    <article class="post">
      <div class="post-image" role="img" aria-label="Photo of a woman underwater with floating hair" style="background:linear-gradient(160deg,#5fc1c0,#2f7f86 55%,#b88a78)"></div>
      <h3 class="post-title">Street Musicians in Black and White</h3>
      <p class="post-summary">I have been more interested with photography since I got a new camera. It's always exciting to capture moments, walk on the streets and find great subjects. I am also always look for</p>
    </article>
    <article class="post">
      <div class="post-image" role="img" aria-label="Photo of a rainbow coloured rose lying in snow" style="background:linear-gradient(150deg,#2c4454,#7e95a6 50%,#d6dde4)"></div>
      <h3 class="post-title">Daily Inspiration Colorful Flower</h3>
      <p class="post-summary">This post is part of our daily series of posts showing the most inspiring images selected by some of the Quenlatori's writers and users. If you want to participate and share your graphic design</p>
    </article>
    <article class="post">
      <div class="post-image" role="img" aria-label="Photo of a turquoise vintage car parked by bare trees" style="background:linear-gradient(180deg,#b9a58c,#7fb9b4 55%,#6c6a55)"></div>
      <h3 class="post-title">Playwave brings a clean new look to ...</h3>
      <p class="post-summary">Editors and contributors share their thoughts on the national pavilions at the Lugano Triennale and 'The Atlas of Rooms' curated by Renzo Albani.</p>
    </article>
  </div>
</section>

<section class="category" style="top:712px">
  <h2 class="category-label">Security</h2>
  <div class="posts">
    <article class="post">
      <div class="post-image" role="img" aria-label="Black and white photo of a person reading a newspaper" style="background:linear-gradient(160deg,#2a2a2a,#9a9a9a 55%,#e0e0e0)"></div>
      <h3 class="post-title">Street Musicians in Black and White</h3>
      <p class="post-summary">I have been more interested with photography since I got a new camera. It's always exciting to capture moments, walk on the streets and find great subjects. I am also always look for</p>
    </article>
    <article class="post">
      <div class="post-image" role="img" aria-label="Photo of two people in costume uniforms against a grey wall" style="background:linear-gradient(170deg,#c9c4bd,#8e8a80 55%,#4f4a3e)"></div>
      <h3 class="post-title">Daily Inspiration Colorful Flower</h3>
      <p class="post-summary">This post is part of our daily series of posts showing the most inspiring images selected by some of the Quenlatori's writers and users. If you want to participate and share your graphic design</p>
    </article>
    <article class="post">
      <div class="post-image" role="img" aria-label="Photo of a street with posters on a wall and a parked car" style="background:linear-gradient(160deg,#c19a72,#a9a39a 50%,#5d5852)"></div>
      <h3 class="post-title">Playwave brings a clean new look to ...</h3>
      <p class="post-summary">Editors and contributors share their thoughts on the national pavilions at the Lugano Triennale and 'The Atlas of Rooms' curated by Renzo Albani.</p>
    </article>
  </div>
</section>

<section class="category" style="top:1205px">
  <h2 class="category-label">Photography</h2>
  <div class="posts">
    <article class="post">
      <div class="post-image" role="img" aria-label="Photo of a soldier kneeling above a mountain town" style="background:linear-gradient(180deg,#d8d8da,#8a8478 50%,#6b5a45)"></div>
      <h3 class="post-title">Street Musicians in Black and White</h3>
      <p class="post-summary">I have been more interested with photography since I got a new camera. It's always exciting to capture moments, walk on the streets and find great subjects. I am also always look for</p>
    </article>
    <article class="post">
      <div class="post-image" role="img" aria-label="Close-up photo of a metal lock on a blue painted door" style="background:radial-gradient(circle at 55% 50%,#b8b2a4 0,#8a9cad 35%,#5f86ad 80%)"></div>
      <h3 class="post-title">Daily Inspiration Colorful Flower</h3>
      <p class="post-summary">This post is part of our daily series of posts showing the most inspiring images selected by some of the Quenlatori's writers and users. If you want to participate and share your graphic design</p>
    </article>
    <article class="post">
      <div class="post-image" role="img" aria-label="High contrast black and white photo of a figure in motion" style="background:linear-gradient(135deg,#111,#d6d6d6 45%,#222 80%)"></div>
      <h3 class="post-title">Playwave brings a clean new look to ...</h3>
      <p class="post-summary">Editors and contributors share their thoughts on the national pavilions at the Lugano Triennale and 'The Atlas of Rooms' curated by Renzo Albani.</p>
    </article>
  </div>
</section>

<section class="category" style="top:1695px">
  <h2 class="category-label">Music</h2>
  <div class="posts">
    <article class="post">
      <div class="post-image" role="img" aria-label="Photo of a singer posed among green jungle leaves" style="background:linear-gradient(160deg,#8fbf5a,#4f8a34 55%,#c9a27a)"></div>
      <h3 class="post-title">Lina Corr – Wildfire</h3>
      <p class="post-summary">I have been more interested with photography since I got a new camera. It's always exciting to capture moments, walk on the streets and find great subjects. I am also always look for</p>
    </article>
    <article class="post">
      <div class="post-image" role="img" aria-label="Photo of a performer seated on a large grey metal ball" style="background:linear-gradient(170deg,#4a4a4a,#8e8e8c 50%,#c0bcb6)"></div>
      <h3 class="post-title">Tessa Rowe – Iron Swing</h3>
      <p class="post-summary">This post is part of our daily series of posts showing the most inspiring images selected by some of the Quenlatori's writers and users. If you want to participate and share your graphic design</p>
    </article>
    <article class="post">
      <div class="post-image" role="img" aria-label="Photo of a four-piece band standing outdoors" style="background:linear-gradient(180deg,#c9c2b4,#6f655a 55%,#2e2a26)"></div>
      <h3 class="post-title">NORTHBOUND – Daylight</h3>
      <p class="post-summary">Editors and contributors share their thoughts on the national pavilions at the Lugano Triennale and 'The Atlas of Rooms' curated by Renzo Albani.</p>
    </article>
  </div>
</section>

<footer class="site-footer">
  <div class="newsletter">
    <h4 class="footer-heading"><strong>Subscribe</strong> to our newsletter</h4>
    <p>At vero eos et accusamus et iusto odio dignissimos ducimus, qui blanditiis praesentium voluptatum deleniti atque corrupti, quos dolores et quas molestias excepturi sint."</p>
  </div>
  <div class="newsletter-form">
    <div class="newsletter-input"></div>
    <div class="newsletter-button">Notify me</div>
  </div>
  <div class="location">
    <h4 class="footer-heading"><strong>Our</strong> location</h4>
    <address>412 Fernlow Street<br>Dunmere, K17 3LP.<br>Phone: +1 555 010 2847</address>
  </div>
  <div class="social social-footer">
    <span class="social-item">Chirp</span>
    <span class="social-item">Facet</span>
    <span class="social-item">Plusly</span>
    <span class="social-item">Pinora</span>
    <span class="social-item">Linkro</span>
  </div>
  <div class="footer-rule"></div>
  <nav class="footer-nav">
    <span>Home</span><span>Photogrpahy</span><span>Politics</span><span>Security</span><span>Music</span>
  </nav>
  <div class="copyright"><strong>Gavin Marsh</strong> © 2013. All Rights Reserved</div>
</footer>

</body>
</html>
```